Business Card Design Project

Business card design based on the existing logo.

Target Market(s)

Small to medium business owners and CIO's looking for professional IT services.

Industry/Entity Type

Business

Font styles to use
Serif
Sans Serif

Requirements
Must have
• Logo, company name, company details

Text to appear on the business card
Name / Title:
Leon Fairholt
CEO

Address:
Valtiro Limited
Level 3, 42 Kestle St
P O Box 462
Paraparaumu 5391

Other details:
leon@valtiro.co
Ph: 0800 519 308
Mob: +64 21 948 216
www.valtiro.co

Nice to have
• I would look at both single and double sided options. My initial thought is double sided with just the logo with the grey framing for the front and the name and details on the back. But I'm open to other design options.

```html
<!DOCTYPE html>
<html lang="en">
<head>
<meta charset="utf-8">
<title>Valtiro Business Cards</title>
<link rel="stylesheet" href="https://fonts.googleapis.com/css2?family=Open+Sans:wght@300;400;600&display=swap">
<style>
  :root {
    --bg: #ecebe8;
    --paper: #ffffff;
    --ink: #3d3d3d;
    --ink-soft: #6b6b6b;
    --brand: #1b6182;
    --brand-deep: #0f4a66;
    --brand-light: #22739a;
    --divider: #8a8a8a;
  }
  * { box-sizing: border-box; margin: 0; padding: 0; }
  html, body {
    width: 1200px; height: 1024px; overflow: hidden;
    background: var(--bg);
    font-family: "Open Sans", Arial, sans-serif;
  }
  .canvas {
    position: relative; width: 1200px; height: 1024px;
    display: flex; align-items: center; justify-content: center; gap: 30px;
  }
  .card {
    position: relative; width: 540px; height: 330px; overflow: hidden;
    box-shadow: 0 6px 18px rgba(0,0,0,.18);
  }
  /* Details side */
  .card--details { background: var(--paper); }
  .card__wave { position: absolute; inset: 0; width: 100%; height: 100%; }
  .wordmark {
    display: flex; align-items: center; gap: 12px;
    font-weight: 300; letter-spacing: 1px;
  }
  .wordmark__dot { border-radius: 50%; flex: none; }
  .card--details .wordmark {
    position: absolute; left: 36px; top: 112px;
    font-size: 40px; color: var(--ink);
  }
  .card--details .wordmark__dot { width: 22px; height: 22px; background: var(--brand); }
  .divider {
    position: absolute; left: 250px; top: 30px; height: 170px;
    border-left: 2px dotted var(--divider);
  }
  .contact { position: absolute; left: 270px; top: 28px; color: var(--ink); }
  .contact__name { font-size: 19px; color: var(--brand); font-weight: 400; }
  .contact__role { font-size: 14px; color: var(--ink); }
  .contact__sep { color: var(--ink-soft); margin: 0 3px; }
  .contact__list { list-style: none; margin-top: 10px; }
  .contact__item {
    display: flex; align-items: flex-start; gap: 9px;
    font-size: 11.5px; line-height: 1.5; margin-bottom: 3px;
  }
  .contact__icon { width: 13px; height: 13px; flex: none; margin-top: 2px; fill: var(--ink-soft); }
  /* Logo side */
  .card--logo {
    background: radial-gradient(ellipse at 40% 35%, var(--brand-light) 0%, var(--brand) 50%, var(--brand-deep) 100%);
    display: flex; align-items: center; justify-content: center;
  }
  .card--logo .wordmark { font-size: 64px; color: #ffffff; gap: 18px; }
  .card--logo .wordmark__dot { width: 32px; height: 32px; background: #ffffff; }
</style>
</head>
<body>
<main class="canvas">
  <section class="card card--details" aria-label="Business card, details side">
    <svg class="card__wave" viewBox="0 0 540 330" preserveAspectRatio="none" aria-hidden="true">
      <path d="M0 282 C200 292 355 266 432 208 C482 168 500 75 522 0 L540 0 L540 330 L0 330 Z" fill="var(--brand)"/>
      <path d="M0 298 C200 308 365 284 448 222 C498 182 515 85 540 12 L540 30 C522 95 508 190 458 232 C375 296 200 318 0 312 Z" fill="#ffffff"/>
    </svg>
    <div class="wordmark"><span class="wordmark__dot"></span>Valtiro</div>
    <div class="divider"></div>
    <div class="contact">
      <p><span class="contact__name">Leon Fairholt</span><span class="contact__sep">|</span><span class="contact__role">CEO</span></p>
      <ul class="contact__list">
        <li class="contact__item">
          <svg class="contact__icon" viewBox="0 0 16 16"><path d="M3 1h3l1.5 4-2 1.3a9 9 0 0 0 4.2 4.2L11 8.5l4 1.5v3a2 2 0 0 1-2 2A13 13 0 0 1 1 3a2 2 0 0 1 2-2z"/></svg>
          <span>0800 519 308</span>
        </li>
        <li class="contact__item">
          <svg class="contact__icon" viewBox="0 0 16 16"><path d="M4 0h8a1 1 0 0 1 1 1v14a1 1 0 0 1-1 1H4a1 1 0 0 1-1-1V1a1 1 0 0 1 1-1zm1 2v10h6V2zm3 11a1 1 0 1 0 0 2 1 1 0 0 0 0-2z"/></svg>
          <span>+64 21 948 216</span>
        </li>
        <li class="contact__item">
          <svg class="contact__icon" viewBox="0 0 16 16"><path d="M1 3h14v10H1zm1.5 1.2V5l5.5 4 5.5-4v-.8z"/></svg>
          <span>leon@valtiro.co</span>
        </li>
        <li class="contact__item">
          <svg class="contact__icon" viewBox="0 0 16 16"><path d="M8 0a8 8 0 1 0 0 16A8 8 0 0 0 8 0zm0 1.5c.9 0 2 1.7 2.3 4.5H5.7C6 3.2 7.1 1.5 8 1.5zM1.6 7h2.9c0 .7 0 1.4.1 2H1.6a6.5 6.5 0 0 1 0-2zm4 0h4.8a14 14 0 0 1 0 2H5.6a14 14 0 0 1 0-2zm5.9 0h2.9a6.5 6.5 0 0 1 0 2h-2.9c.1-.6.1-1.3 0-2zM5.7 10h4.6c-.3 2.8-1.4 4.5-2.3 4.5s-2-1.7-2.3-4.5z"/></svg>
          <span>www.valtiro.co</span>
        </li>
        <li class="contact__item">
          <svg class="contact__icon" viewBox="0 0 16 16"><path d="M8 0a5.5 5.5 0 0 0-5.5 5.5C2.5 10 8 16 8 16s5.5-6 5.5-10.5A5.5 5.5 0 0 0 8 0zm0 8a2.5 2.5 0 1 1 0-5 2.5 2.5 0 0 1 0 5z"/></svg>
          <span>Level 3, 42 Kestle St,<br>P O Box 462<br>Paraparaumu 5391</span>
        </li>
      </ul>
    </div>
  </section>

  <section class="card card--logo" aria-label="Business card, logo side">
    <div class="wordmark"><span class="wordmark__dot"></span>Valtiro</div>
  </section>
</main>
</body>
</html>
```